New Solo Law Office Needs Business Card/Letterhead Design

I am starting a solo law office called "Law Office of Conrad Vashti, PLLC" in Tucson, Arizona. I will be doing criminal defense trial work. More than a logo with any sort of icon, I am really just looking for the name of the company to be displayed in a sleek, minimalist but interesting sort of way, with a format and font type that communicates professionalism. It can be in color, but doesn't have to be, and I am thinking blue and/or red accents colors. I'd like it to convey that I am passionate, dependable and willing to fight. For the business card, I envision sort of higher quality card material, and maybe some embossing or raised print. I will want to include my company name, name, phone and fax numbers, email and website addresses. For the letterhead, I will want to be able to use the same sort of font/formatting design as on the business card.
Industry/Entity Type
Business
Contact Information for Business Card
Law Office of Conrad Vashti, PLLC
Conrad Vashti
conrad@vashti-law.example
www.vashti-law.example
(I do not yet have an established phone or fax number, so please put in some place holder numbers for the formatting, and I can add the actual numbers in before I print.)
Colors
Designer to choose colors to be used in the design.
Look and feel

```html
<!DOCTYPE html>
<html lang="en">
<head>
<meta charset="utf-8">
<title>Law Office of Conrad Vashti, PLLC — Business Card</title>
<link rel="stylesheet" href="https://fonts.googleapis.com/css2?family=Cinzel:wght@400;500&family=Open+Sans:wght@400;800&display=swap">
<style>
  :root {
    --canvas: #141414;
    --frame: #b4b4b4;
    --card-core: #2b2b2b;
    --card-edge: #050505;
    --ink: #f2f2f2;
    --ink-soft: #cfcfcf;
    --rule: rgba(255,255,255,0.55);
    --label-bar: #121212;
  }
  * { margin: 0; padding: 0; box-sizing: border-box; }
  html, body { width: 1200px; height: 1200px; overflow: hidden; background: var(--canvas); }
  h1, h2, p { font-weight: 400; }
  .presentation {
    position: absolute; left: 0; top: 370px; width: 1200px;
  }
  .card-row {
    display: flex; gap: 8px; padding: 6px; background: var(--frame);
  }
  .card {
    position: relative; width: 590px; height: 360px; overflow: hidden;
    background:
      radial-gradient(ellipse 60% 55% at 50% 48%, var(--card-core) 0%, #141414 60%, var(--card-edge) 100%);
    color: var(--ink);
    text-align: center;
  }
  .card--back .firm-name {
    position: absolute; left: 0; right: 0; top: 168px;
    font-family: "Cinzel", serif; font-weight: 400; font-size: 22px; letter-spacing: 0.5px; color: var(--ink-soft);
  }
  .card--back .firm-rule {
    position: absolute; left: 150px; right: 150px; top: 198px; height: 1px;
    background: linear-gradient(90deg, transparent, var(--rule), transparent);
  }
  .card--back .firm-web {
    position: absolute; left: 0; right: 0; top: 202px;
    font-family: "Open Sans", sans-serif; font-size: 14px; letter-spacing: 1.2px; color: var(--ink-soft);
  }
  .card--front .firm-title {
    position: absolute; left: 0; right: 0; top: 66px;
    font-family: "Open Sans", sans-serif; font-weight: 400; font-size: 27px; color: var(--ink);
  }
  .card--front .title-glow {
    position: absolute; left: 60px; right: 60px; top: 108px; height: 1px;
    background: linear-gradient(90deg, transparent, rgba(255,255,255,0.12), transparent);
  }
  .attorney-name {
    position: absolute; left: 0; right: 0; top: 150px;
    font-family: "Cinzel", serif; font-size: 31px; letter-spacing: 1px;
  }
  .name-rule {
    position: absolute; left: 175px; right: 175px; top: 192px; height: 1px;
    background: linear-gradient(90deg, transparent, var(--rule), transparent);
  }
  .contact-list {
    position: absolute; left: 0; right: 0; top: 196px; list-style: none;
    font-family: "Open Sans", sans-serif; font-size: 16px; line-height: 20px;
  }
  .contact-list li { display: flex; justify-content: center; align-items: center; gap: 6px; }
  .contact-list li:first-child { font-size: 17px; margin-bottom: 2px; }
  .contact-list svg { width: 14px; height: 14px; flex: none; }
  .footer-glow {
    position: absolute; left: 0; right: 0; bottom: 0; height: 48px;
    background: radial-gradient(ellipse 50% 100% at 50% 100%, rgba(255,255,255,0.16), transparent 70%);
  }
  .footer-line {
    position: absolute; left: 80px; right: 80px; top: 318px; height: 1px;
    background: linear-gradient(90deg, transparent, rgba(255,255,255,0.5), transparent);
  }
  .footer-web {
    position: absolute; left: 0; right: 0; top: 326px;
    display: flex; justify-content: center; align-items: center; gap: 6px;
    font-family: "Open Sans", sans-serif; font-size: 14px; letter-spacing: 1px;
  }
  .footer-web::before, .footer-web::after { content: ""; width: 128px; height: 1px; }
  .footer-web::before { background: linear-gradient(90deg, transparent, #d8d8d8); }
  .footer-web::after { background: linear-gradient(90deg, #d8d8d8, transparent); }
  .side-labels {
    display: flex; background: var(--label-bar); border-bottom: 12px solid var(--frame);
  }
  .side-labels span {
    flex: 1; text-align: center; padding: 8px 0 10px;
    font-family: "Open Sans", sans-serif; font-weight: 800; font-size: 40px; color: #fff;
    letter-spacing: 1px;
  }
</style>
</head>
<body>
  <main class="presentation">
    <section class="card-row">
      <article class="card card--back" aria-label="Card back">
        <h1 class="firm-name">LAW OFFICE OF CONRAD VASHTI, PLLC</h1>
        <div class="firm-rule"></div>
        <p class="firm-web">www.vashti-law.example</p>
      </article>
      <article class="card card--front" aria-label="Card front">
        <h2 class="firm-title">Law Office of Conrad Vashti, PLLC</h2>
        <div class="title-glow"></div>
        <p class="attorney-name">Conrad Vashti</p>
        <div class="name-rule"></div>
        <ul class="contact-list">
          <li>
            <svg viewBox="0 0 16 16" aria-hidden="true"><rect x="1" y="3" width="14" height="10" fill="none" stroke="#fff" stroke-width="1.3"/><path d="M1 3l7 6 7-6M1 13l5-5M15 13l-5-5" fill="none" stroke="#fff" stroke-width="1.1"/></svg>
            conrad@vashti-law.example
          </li>
          <li>
            <svg viewBox="0 0 16 16" aria-hidden="true"><rect x="4" y="1" width="8" height="14" rx="1.5" fill="none" stroke="#fff" stroke-width="1.5"/><line x1="6.5" y1="12.5" x2="9.5" y2="12.5" stroke="#fff" stroke-width="1"/></svg>
            520 5550 1420
          </li>
          <li>
            <svg viewBox="0 0 16 16" aria-hidden="true"><rect x="1" y="6" width="14" height="8" rx="1" fill="#fff"/><rect x="4" y="2" width="8" height="5" fill="none" stroke="#fff" stroke-width="1.3"/><rect x="3.5" y="9" width="9" height="2" fill="#111"/></svg>
            520 5550 1421
          </li>
        </ul>
        <div class="footer-glow"></div>
        <div class="footer-line"></div>
        <p class="footer-web">www.vashti-law.example</p>
      </article>
    </section>
    <div class="side-labels">
      <span>back</span>
      <span>front</span>
    </div>
  </main>
</body>
</html>
```